Branding flyers and marketing brochure templates

We are after corporate design templates for the following: 1. Flyer to advertise a course - include course name, course unit code, summary of course, entry requirements, price, course description. 2. Price list - to use for each office location, listing all courses - include course name, course unit code, date/time, price - also include section/key to notify for each course if funding is available 3. Marketing flyer template - to advertise government funding options that we have which a student may be eligible for (see 'funding' tab on our webpage marlowtrain.edu.au - we need one for each Skillpath 5 Pledge and Trade Bridge. We want each of these templates to have similar designs and branding. There will be future work involved for creating more templates of similar branding for the correct person.

Files must be editable, preferably given as word, publisher or editable pdf.

9bcb3c

• Green

```html
<!DOCTYPE html>
<html lang="en">
<head>
<meta charset="utf-8">
<title>Price List – Marlowtrain Safety and Training</title>
<link href="https://fonts.googleapis.com/css2?family=Fira+Sans+Condensed:wght@400;600;800&family=Open+Sans:wght@400;600&display=swap" rel="stylesheet">
<style>
  :root{
    --backdrop:#f6c4a8;
    --green:#8cc63f;
    --green-deep:#5f9e22;
    --red:#ec2733;
    --yellow:#ffe500;
    --ink:#111111;
    --paper:#ffffff;
    --paper-grey:#f1f1f1;
    --photo-a:#c9ccd1;
    --photo-b:#e8a46a;
  }
  *{box-sizing:border-box;margin:0;padding:0}
  html,body{width:1200px;height:960px;overflow:hidden;background:var(--backdrop)}
  .sheet{
    position:absolute;left:282px;top:30px;width:636px;height:900px;
    background:linear-gradient(180deg,var(--paper-grey),var(--paper) 40%);
    overflow:hidden;font-family:"Open Sans",sans-serif;
    box-shadow:0 10px 30px rgba(0,0,0,.18);
  }
  .header-band,.footer-band{position:absolute;left:0;width:636px}
  .header-band{top:0;height:200px}
  .footer-band{bottom:0;height:140px}
  .brand{
    position:absolute;left:28px;top:30px;display:flex;align-items:center;gap:12px;
  }
  .brand-dot{width:46px;height:46px;border-radius:50%;background:var(--yellow)}
  .brand-text{display:flex;flex-direction:column}
  .brand-name{
    font-family:"Fira Sans Condensed",sans-serif;font-weight:800;font-size:42px;
    line-height:1;color:var(--yellow);letter-spacing:1px;
  }
  .brand-sub{
    font-family:"Fira Sans Condensed",sans-serif;font-weight:400;font-size:15px;
    color:#fff;letter-spacing:4px;margin-top:4px;
  }
  .brand-locations{
    position:absolute;left:86px;top:106px;font-family:"Fira Sans Condensed",sans-serif;
    font-size:10.5px;color:#fff;letter-spacing:.3px;
  }
  .brand-meta{
    position:absolute;left:150px;top:122px;font-family:"Fira Sans Condensed",sans-serif;
    font-size:7.5px;color:#fff;
  }
  .head-office{
    position:absolute;right:20px;top:18px;text-align:right;color:#fff;font-style:normal;
    font-family:"Fira Sans Condensed",sans-serif;font-size:8px;line-height:1.4;
  }
  .head-office .label{font-size:9px;letter-spacing:.5px}
  .head-office .email{display:flex;align-items:center;justify-content:flex-end;gap:4px;margin-top:4px}
  .photo-area{
    position:absolute;left:40px;top:470px;width:596px;height:360px;
    background:linear-gradient(110deg,var(--photo-a) 0%,#dfe1e4 45%,var(--photo-b) 75%,var(--photo-a) 100%);
    opacity:.35;
  }
  .title-bar{
    position:absolute;left:34px;top:222px;width:568px;height:62px;border-radius:12px;
    background:var(--red);color:#fff;text-align:center;
    font-family:"Fira Sans Condensed",sans-serif;font-weight:600;font-size:42px;line-height:62px;letter-spacing:.5px;
  }
  .price-table{
    position:absolute;left:36px;top:302px;width:562px;
    border-collapse:separate;border-spacing:0;border:2px solid var(--ink);border-radius:12px;
    font-family:"Fira Sans Condensed",sans-serif;
  }
  .price-table th,.price-table td{border-right:1.5px solid var(--ink);border-bottom:1.5px solid var(--ink)}
  .price-table th:last-child,.price-table td:last-child{border-right:none}
  .price-table tr:last-child td{border-bottom:none}
  .price-table th{
    height:62px;font-weight:400;font-size:22px;color:var(--ink);padding:0 6px;white-space:nowrap;
  }
  .price-table td{height:42px}
  .col-name{width:110px}.col-code{width:134px}.col-date{width:112px}.col-price{width:70px}
  .tagline{
    position:absolute;left:0;right:0;bottom:30px;text-align:center;color:#fff;
    font-family:"Open Sans",sans-serif;font-weight:600;font-size:17px;letter-spacing:3px;
  }
</style>
</head>
<body>
<main class="sheet">
  <div class="photo-area" role="img" aria-label="Faded photo of two construction workers in hard hats and hi-vis vests in front of high-rise buildings"></div>

  <svg class="header-band" viewBox="0 0 636 200" aria-hidden="true">
    <defs>
      <linearGradient id="headGreen" x1="0" y1="0" x2="0" y2="1">
        <stop offset="0" stop-color="#9ad14a"/><stop offset="1" stop-color="#6fb22a"/>
      </linearGradient>
    </defs>
    <polygon points="0,0 636,0 636,186 568,186 492,132 0,148" fill="url(#headGreen)"/>
    <polyline points="0,148 492,132 568,186 636,186" fill="none" stroke="#ec2733" stroke-width="3"/>
  </svg>

  <div class="brand">
    <span class="brand-dot"></span>
    <div class="brand-text">
      <span class="brand-name">MARLOWTRAIN</span>
      <span class="brand-sub">SAFETY AND TRAINING</span>
    </div>
  </div>
  <p class="brand-locations">KELVALE | DUNMORE | ASHFORD | BRAYSIDE | CORRAN | WESTBY | NORLUN</p>
  <p class="brand-meta">RTO#00000 &nbsp;|&nbsp; www.marlowtrain.edu.au &nbsp;|&nbsp; 1300 MARLOW</p>

  <address class="head-office">
    <div class="label">HEAD OFFICE</div>
    <div>ABN 00 000 000 000</div>
    <div>18 Harbour Lane</div>
    <div>Kelvale QLD 4300</div>
    <div class="email">
      <svg width="9" height="7" viewBox="0 0 9 7" aria-hidden="true"><rect x=".5" y=".5" width="8" height="6" fill="none" stroke="#fff"/><polyline points=".5,.5 4.5,4 8.5,.5" fill="none" stroke="#fff"/></svg>
      info@marlowtrain.edu.au
    </div>
  </address>

  <svg class="footer-band" viewBox="0 0 636 140" aria-hidden="true">
    <defs>
      <linearGradient id="footGreen" x1="0" y1="0" x2="0" y2="1">
        <stop offset="0" stop-color="#84c23a"/><stop offset="1" stop-color="#5f9e22"/>
      </linearGradient>
    </defs>
    <polygon points="0,0 22,6 68,64 636,74 636,140 0,140" fill="url(#footGreen)"/>
    <polyline points="0,0 22,6 68,64 636,74" fill="none" stroke="#ec2733" stroke-width="3"/>
  </svg>

  <h1 class="title-bar">PRICE LIST</h1>

  <table class="price-table">
    <thead>
      <tr>
        <th class="col-name">Course name</th>
        <th class="col-code">Course unit code</th>
        <th class="col-date">Date/time</th>
        <th class="col-price">Price</th>
        <th class="col-key">Section/key</th>
      </tr>
    </thead>
    <tbody>
      <tr><td></td><td></td><td></td><td></td><td></td></tr>
      <tr><td></td><td></td><td></td><td></td><td></td></tr>
      <tr><td></td><td></td><td></td><td></td><td></td></tr>
      <tr><td></td><td></td><td></td><td></td><td></td></tr>
      <tr><td></td><td></td><td></td><td></td><td></td></tr>
      <tr><td></td><td></td><td></td><td></td><td></td></tr>
      <tr><td></td><td></td><td></td><td></td><td></td></tr>
      <tr><td></td><td></td><td></td><td></td><td></td></tr>
      <tr><td></td><td></td><td></td><td></td><td></td></tr>
      <tr><td></td><td></td><td></td><td></td><td></td></tr>
      <tr><td></td><td></td><td></td><td></td><td></td></tr>
    </tbody>
  </table>

  <p class="tagline">Building skills for safer worksites</p>
</main>
</body>
</html>
```